Wohnhof am Weiher - Zeitungsinserat für den Verkauf von Eigentumswohnungen

Wir brauchen ein Zeitungsinserat in zwei Formaten. Einmal 296 Breite x 440 Höhe mm und einmal 296 Breite x 220 mm Höhe.
Als Basis dient der sehr grobe Entwurf im Powerpoint (Entwurf.pptx).
Auf dem Entwurf fehlen noch die Kontaktangeben:
Brunnhofer Liegenschaften AG
Seematteweg 14
4387 Tannried
079 462 37 58
rbrunnhofer@tessin-ostwald.ch

Zudem muss noch der Link auf die Webseite aufgeführt werden.
www.wohnhof-am-weiher.ch

Zudem fehlt noch der Text:
Fordern Sie noch heute die Verkaufsunterlagen gedruckt oder per Email an. Schreiben Sie uns einfach eine Chatpost mit Ihrer Adresse.

Ich habe noch Files von den Innenvisualisierungen, den Aussenvisualisierungen sowie unser Logo hinzugefügt. Zudem habe ich Ihnen die Verkaufsbrochure angefügt. Sie können die Daten vom Entwurf gerne ergänzen wenn Ihnen etwas gefällt. Schön wäre es, wenn Sie den Stil ähnlich machen würden wie die Brochure.

Target Market(s)

Famillien, Paare und Rentner

Font styles to use
Serif

Colors

Designer to choose colors to be used in the design.

Requirements
Must have
• Tolles Design das sofort anspricht!

```html
<!DOCTYPE html>
<html lang="de">
<head>
<meta charset="utf-8">
<title>Wohnhof am Weiher – Inserat</title>
<link rel="stylesheet" href="https://fonts.googleapis.com/css2?family=Poppins:wght@400;500;600;700;800&display=swap">
<style>
  :root{
    --page:#eceef1;
    --paper:#ffffff;
    --navy:#10688f;
    --red:#e5202a;
    --band:#1b8fd5;
    --rule:#5eaee2;
    --ink:#111418;
    --muted:#3a4048;
  }
  *{box-sizing:border-box;margin:0;padding:0}
  html,body{width:692px;height:1200px;overflow:hidden;background:var(--page);font-family:"Poppins",sans-serif;color:var(--ink)}
  .ad{position:absolute;left:0;top:368px;width:692px;height:464px;background:var(--paper);box-shadow:0 6px 18px rgba(0,0,0,.18);overflow:hidden}
  .hero{position:absolute;left:0;top:0;width:692px;height:223px;
    background:linear-gradient(180deg,#f4f8fb 0%,#e6eef4 32%,#c9d3d8 55%,#a7adaa 70%,#7f9a66 86%,#5f8a3e 100%)}
  .title{position:absolute;left:38px;top:30px;font-weight:800;font-size:44px;letter-spacing:-.5px;line-height:1;white-space:nowrap}
  .title .a{color:var(--navy)}
  .title .b{color:var(--red)}
  .band{position:absolute;left:0;top:223px;width:692px;height:66px;background:var(--band);display:flex;padding:7px 10px 0 36px;color:#fff}
  .feature{padding:0 8px;border-left:1px solid rgba(255,255,255,.7);height:52px}
  .feature:first-child{border-left:none;padding-left:0}
  .f1{width:103px}.f2{width:122px}.f3{width:119px}.f4{width:150px}.f5{flex:1}
  .feature h3{font-size:9.4px;font-weight:700;line-height:1.2;display:flex;gap:4px;align-items:flex-start;margin-bottom:3px}
  .feature h3 svg{flex:none;margin-top:1px}
  .feature p{font-size:4.1px;line-height:1.35;padding-left:12px}
  .house{position:absolute;top:298px;width:199px}
  .house .tab{display:block;margin:0 auto;width:48px;height:11px;border-radius:3px 3px 0 0;background:var(--band);color:#fff;font-size:9px;font-weight:700;line-height:11px;text-align:center}
  table{width:100%;border-collapse:collapse;border:1px solid var(--rule)}
  td{border:.6px solid var(--rule);font-size:4.1px;line-height:1.25;padding:2px 3px;vertical-align:middle;color:var(--muted)}
  td:nth-child(1){width:21%}td:nth-child(2){width:20%}td:nth-child(3){width:13%}td:nth-child(4){width:27%}
  .footer{position:absolute;left:0;top:398px;width:692px;height:50px}
  .brand{position:absolute;left:34px;top:12px;display:flex;align-items:center;gap:4px;color:var(--navy);font-weight:600;font-size:8.4px;line-height:1.15}
  .brand i{display:block;width:9px;height:9px;background:var(--navy)}
  .cta{position:absolute;left:138px;top:4px;width:272px;font-size:7.6px;line-height:1.3;color:var(--ink)}
  .cta .mail{display:flex;align-items:center;gap:4px;font-weight:700;font-size:9.6px;margin-top:1px;white-space:nowrap}
  .divider{position:absolute;left:413px;top:4px;width:1px;height:36px;background:#9aa3ab}
  .company{position:absolute;left:419px;top:4px;font-weight:700;font-size:8.4px;line-height:1.2;white-space:nowrap}
  .company .phone{display:flex;align-items:center;gap:3px;font-size:12.6px;margin-top:1px}
  .address{position:absolute;left:563px;top:4px;display:flex;gap:4px;font-weight:700;font-size:8.4px;line-height:1.2;white-space:nowrap}
  .web{position:absolute;left:563px;top:30px;font-weight:700;font-size:7.4px;line-height:1.2;color:var(--navy);white-space:nowrap}
</style>
</head>
<body>
<main class="ad">
  <div class="hero" role="img" aria-label="Aussenvisualisierung der Wohnanlage mit drei Mehrfamilienhäusern, Garten und Bäumen"></div>
  <h1 class="title"><span class="a">WOHNHOF</span> <span class="b">AM WEIHER</span></h1>

  <section class="band">
    <div class="feature f1"><h3><svg width="8" height="8" viewBox="0 0 10 10"><circle cx="5" cy="5" r="4.3" fill="none" stroke="#fff" stroke-width="1"/><path d="M3 5.1l1.4 1.4L7.2 3.7" fill="none" stroke="#fff" stroke-width="1"/></svg>Bus und Bahn</h3>
      <p>Der Bahnhof liegt nahe und bietet gute Zugverbindungen in die Stadt, in wenigen Minuten mit dem Bus zu erreichen.</p></div>
    <div class="feature f2"><h3><svg width="8" height="8" viewBox="0 0 10 10"><circle cx="5" cy="5" r="4.3" fill="none" stroke="#fff" stroke-width="1"/><path d="M3 5.1l1.4 1.4L7.2 3.7" fill="none" stroke="#fff" stroke-width="1"/></svg>Basel – Stadt</h3>
      <p>Der nahe Bahnhof verfügt über sehr gute Verbindungen in die Stadt, welche durch den Ausbau künftig noch verbessert werden.</p></div>
    <div class="feature f3"><h3><svg width="8" height="8" viewBox="0 0 10 10"><circle cx="5" cy="5" r="4.3" fill="none" stroke="#fff" stroke-width="1"/><path d="M3 5.1l1.4 1.4L7.2 3.7" fill="none" stroke="#fff" stroke-width="1"/></svg>Autobahn</h3>
      <p>Die Wohnsiedlung ist ideal auch für den Individualverkehr erschlossen. Die nächste Autobahneinfahrt ist in wenigen Minuten erreichbar.</p></div>
    <div class="feature f4"><h3><svg width="8" height="8" viewBox="0 0 10 10"><circle cx="5" cy="5" r="4.3" fill="none" stroke="#fff" stroke-width="1"/><path d="M3 5.1l1.4 1.4L7.2 3.7" fill="none" stroke="#fff" stroke-width="1"/></svg><span>Einkaufen und weitere<br>Dienstleistungen</span></h3>
      <p>Durch die Nähe zum Dorfzentrum liegen Einkaufsmöglichkeiten und Dienstleistungen in maximal zwei Minuten Fahrzeit oder zehn Minuten Gehdistanz.</p></div>
    <div class="feature f5"><h3><svg width="8" height="8" viewBox="0 0 10 10"><circle cx="5" cy="5" r="4.3" fill="none" stroke="#fff" stroke-width="1"/><path d="M3 5.1l1.4 1.4L7.2 3.7" fill="none" stroke="#fff" stroke-width="1"/></svg>Erholung im Grünen</h3>
      <p>Tannried erfüllt mit Wäldern, offenen Feldern, Wander- und Velorouten und ländlicher Ruhe alle Voraussetzungen für ein Naherholungsgebiet.</p></div>
  </section>

  <section class="house" style="left:34px">
    <span class="tab">Haus A</span>
    <table>
      <tr><td>Attika</td><td>4.5 Zimmer</td><td>108m2</td><td>105m2<br>Sonnenterrasse</td><td>945'000 CHF</td></tr>
      <tr><td>Obergeschoss</td><td>3.5 Zimmer</td><td>81m2</td><td>16m2 Balkon</td><td>754'800 CHF</td></tr>
      <tr><td>Obergeschoss</td><td>4.5 Zimmer</td><td>102m2</td><td>33m2 Balkon</td><td>640'000 CHF</td></tr>
      <tr><td>Erdgeschoss</td><td>3.5 Zimmer</td><td>81m2</td><td>16m2<br>gedeckter Sitzplatz<br>&amp; eigener Garten</td><td>657'000 CHF</td></tr>
      <tr><td>Erdgeschoss</td><td>4.5 Zimmer</td><td>102m2</td><td>33m2<br>gedeckter Sitzplatz<br>&amp; eigener Garten</td><td>765'000 CHF</td></tr>
    </table>
  </section>
  <section class="house" style="left:243px">
    <span class="tab">Haus B</span>
    <table>
      <tr><td>Attika</td><td>4.5 Zimmer</td><td>108m2</td><td>105m2<br>Sonnenterrasse</td><td>945'000 CHF</td></tr>
      <tr><td>Obergeschoss</td><td>3.5 Zimmer</td><td>81m2</td><td>16m2 Balkon</td><td>754'800 CHF</td></tr>
      <tr><td>Obergeschoss</td><td>4.5 Zimmer</td><td>102m2</td><td>33m2 Balkon</td><td>640'000 CHF</td></tr>
      <tr><td>Erdgeschoss</td><td>3.5 Zimmer</td><td>81m2</td><td>16m2<br>gedeckter Sitzplatz<br>&amp; eigener Garten</td><td>657'000 CHF</td></tr>
      <tr><td>Erdgeschoss</td><td>4.5 Zimmer</td><td>102m2</td><td>33m2<br>gedeckter Sitzplatz<br>&amp; eigener Garten</td><td>765'000 CHF</td></tr>
    </table>
  </section>
  <section class="house" style="left:451px">
    <span class="tab">Haus C</span>
    <table>
      <tr><td>Attika</td><td>4.5 Zimmer</td><td>108m2</td><td>105m2<br>Sonnenterrasse</td><td>945'000 CHF</td></tr>
      <tr><td>Obergeschoss</td><td>3.5 Zimmer</td><td>81m2</td><td>16m2 Balkon</td><td>754'800 CHF</td></tr>
      <tr><td>Obergeschoss</td><td>4.5 Zimmer</td><td>102m2</td><td>33m2 Balkon</td><td>640'000 CHF</td></tr>
      <tr><td>Erdgeschoss</td><td>3.5 Zimmer</td><td>81m2</td><td>16m2<br>gedeckter Sitzplatz<br>&amp; eigener Garten</td><td>657'000 CHF</td></tr>
      <tr><td>Erdgeschoss</td><td>4.5 Zimmer</td><td>102m2</td><td>33m2<br>gedeckter Sitzplatz<br>&amp; eigener Garten</td><td>765'000 CHF</td></tr>
    </table>
  </section>

  <footer class="footer">
    <div class="brand"><i></i><span>Brunnhofer<br>Liegenschaften AG</span></div>
    <div class="cta">
      Fordern Sie noch heute die Verkaufsunterlagen gedruckt oder per Email an. Schreiben Sie uns einfach eine Chatpost mit Ihrer Adresse
      <div class="mail"><svg width="9" height="7" viewBox="0 0 10 8"><rect x=".5" y=".5" width="9" height="7" rx="1" fill="var(--band)"/><path d="M1 1.2l4 3.2 4-3.2" fill="none" stroke="#fff" stroke-width=".9"/></svg>rbrunnhofer@tessin-ostwald.ch</div>
    </div>
    <div class="divider"></div>
    <div class="company">Brunnhofer Liegenschaften AG
      <div class="phone"><svg width="8" height="8" viewBox="0 0 10 10"><path d="M2.2 1h2l.8 2.2-1.2.9a6 6 0 0 0 2.1 2.1l.9-1.2L9 5.8v2A1.2 1.2 0 0 1 7.8 9 7.6 7.6 0 0 1 1 2.2 1.2 1.2 0 0 1 2.2 1z" fill="var(--band)"/></svg>079 462 37 58</div>
    </div>
    <div class="address"><svg width="9" height="11" viewBox="0 0 10 12"><path d="M5 11S1.2 6.8 1.2 4.4a3.8 3.8 0 0 1 7.6 0C8.8 6.8 5 11 5 11z" fill="none" stroke="var(--band)" stroke-width="1.1"/><circle cx="5" cy="4.4" r="1.3" fill="var(--band)"/></svg><span>Seematteweg 14<br>4387 Tannried</span></div>
    <div class="web">www.wohnhof-am-weiher.ch</div>
  </footer>
</main>
</body>
</html>
```